One Pager Fact Sheet Design

I need a couple of headers and footer designed to use for information security fact sheets to give to customers. Similar to the one listed below.

```html
<!DOCTYPE html>
<html lang="en">
<head>
<meta charset="utf-8">
<title>One Pager Fact Sheet – Brightline Networks</title>
<link rel="stylesheet" href="https://fonts.googleapis.com/css2?family=Lato:wght@400;700&family=Titillium+Web:ital,wght@0,400;0,700;1,400;1,700&display=swap">
<style>
  :root {
    --backdrop: #e9eaeb;
    --paper: #ffffff;
    --brand-red: #e3141b;
    --ink: #2b2b2b;
    --body-ink: #3a3a3a;
    --header-black: #0b0b0c;
    --bar-grey: #3f4042;
    --tagline-grey: #8a8b8d;
    --icon-grey: #c2c3c5;
    --rule: #e4e4e4;
  }
  * { box-sizing: border-box; margin: 0; padding: 0; }
  html, body {
    width: 1200px; height: 752px; overflow: hidden;
    background: var(--backdrop);
  }
  .board { position: relative; width: 1200px; height: 752px; }

  .sheet {
    position: absolute; top: 100px;
    width: 424px; height: 600px;
    background: var(--paper);
    box-shadow: 0 6px 14px rgba(0,0,0,.18);
    overflow: hidden;
    font-family: "Lato", sans-serif;
  }
  .sheet--bold { left: 146px; }
  .sheet--clean { left: 630px; }

  .header { position: absolute; left: 0; top: 0; width: 424px; height: 90px; }
  .header svg { position: absolute; left: 0; top: 0; }

  .earth-photo {
    position: absolute; top: 0; height: 68px;
    background:
      radial-gradient(ellipse 120% 90% at 60% 130%, #3d6fb0 0%, #1d3f6e 35%, #0f2540 55%, transparent 75%),
      linear-gradient(180deg, #0a1a24 0%, #12301f 60%, #0b1a28 100%);
  }
  .sheet--bold .earth-photo {
    left: 200px; width: 224px;
    -webkit-mask-image: linear-gradient(90deg, transparent 0%, #000 45%);
    mask-image: linear-gradient(90deg, transparent 0%, #000 45%);
  }
  .sheet--clean .earth-photo {
    left: 202px; width: 222px;
    clip-path: polygon(24px 0, 100% 0, 100% 100%, 0 100%);
  }

  .brand { position: absolute; display: flex; align-items: center; gap: 6px; white-space: nowrap; }
  .brand__mark {
    border-radius: 50%;
    border: 3px solid var(--brand-red); background: transparent;
  }
  .brand__name {
    font-family: "Titillium Web", sans-serif; font-weight: 700;
    line-height: 1; letter-spacing: -.2px;
  }
  .sheet--bold .brand { left: 37px; top: 22px; }
  .sheet--bold .brand__mark { width: 30px; height: 30px; }
  .sheet--bold .brand__name { color: #ffffff; font-size: 19px; }
  .sheet--clean .brand { left: 18px; top: 26px; gap: 5px; }
  .sheet--clean .brand__mark { width: 26px; height: 26px; }
  .sheet--clean .brand__name { color: var(--brand-red); font-size: 15.5px; }

  .tagline {
    position: absolute;
    font-family: "Titillium Web", sans-serif; font-style: italic; font-weight: 700;
    white-space: nowrap;
  }
  .sheet--bold .tagline { left: 160px; top: 70px; font-size: 12.6px; color: var(--tagline-grey); }
  .sheet--clean .tagline { left: 220px; top: 48px; font-size: 10.4px; color: #ffffff; }
  .tagline__accent { color: var(--brand-red); }

  .content { position: absolute; left: 36px; width: 354px; }
  .sheet--bold .content { top: 133px; }
  .sheet--clean .content { top: 116px; }

  .section-title {
    color: var(--brand-red); font-weight: 700;
    font-size: 9px; line-height: 11px; margin-bottom: 4px;
    text-transform: uppercase;
  }
  .topic-title {
    color: var(--ink); font-weight: 700;
    font-size: 7.6px; line-height: 10px; margin-bottom: 4px;
  }
  .content p {
    color: var(--body-ink); font-size: 6.6px; line-height: 8.55px;
    text-align: justify; margin-bottom: 5.5px;
  }
  .block { margin-bottom: 8px; }
  .block--spaced { margin-bottom: 19px; }
  .topic { margin-bottom: 10px; }

  .features {
    position: absolute; left: 12px; right: 12px; top: 528px; height: 40px;
    border-top: 1px solid var(--rule);
    display: grid; grid-template-columns: 70px 62px 65px 72px 72px 1fr;
    list-style: none;
  }
  .feature {
    display: flex; flex-direction: column; align-items: center;
    padding-top: 5px; border-right: 1px solid var(--rule);
    font-family: "Titillium Web", sans-serif; font-style: italic;
    font-size: 5.8px; line-height: 7px; text-align: center; white-space: nowrap;
  }
  .feature:last-child { border-right: 0; }
  .feature svg { width: 14px; height: 14px; margin-bottom: 2px; fill: var(--icon-grey); }
  .feature__top { color: var(--ink); }
  .feature__bottom { color: var(--brand-red); }

  .contact-bar { position: absolute; left: 0; bottom: 0; width: 424px; height: 29px; }
  .contact-bar svg.contact-bar__shape { position: absolute; left: 0; top: 0; }
  .contact-bar__prompt {
    position: absolute; left: 14px; top: 6px;
    font-family: "Titillium Web", sans-serif; font-style: italic; font-weight: 700;
    color: #ffffff; font-size: 7px; line-height: 8px;
  }
  .contact-list {
    position: absolute; left: 96px; top: 0; height: 29px;
    display: flex; align-items: center; gap: 8px;
    font-family: "Titillium Web", sans-serif; font-size: 7.3px; color: #f2f2f2;
    white-space: nowrap;
  }
  .contact-item { display: flex; align-items: center; gap: 4px; }
  .contact-item svg { width: 6.5px; height: 6.5px; fill: #ffffff; }
</style>
</head>
<body>
<main class="board">

  <!-- Fact sheet: bold header -->
  <article class="sheet sheet--bold">
    <header class="header">
      <svg width="424" height="90" viewBox="0 0 424 90">
        <polygon points="0,16 16,16 0,56" fill="var(--brand-red)"/>
        <polygon points="30,0 424,0 424,68 8,68" fill="var(--header-black)"/>
        <polygon points="0,68 152,68 146,86 0,86" fill="var(--brand-red)"/>
        <g fill="#ffffff">
          <polygon points="46,68 51,68 45,86 40,86"/>
          <polygon points="68,68 73,68 67,86 62,86"/>
          <polygon points="90,68 95,68 89,86 84,86"/>
          <polygon points="112,68 117,68 111,86 106,86"/>
          <polygon points="134,68 139,68 133,86 128,86"/>
        </g>
      </svg>
      <div class="earth-photo" role="img" aria-label="Night view of the Earth from orbit covered by a glowing network of connected points"></div>
      <div class="brand">
        <span class="brand__mark"></span>
        <span class="brand__name">Brightline Networks</span>
      </div>
      <p class="tagline">We Make Your IT-problems Go Away For Good.</p>
    </header>

    <section class="content">
      <div class="block">
        <h2 class="section-title">Summary</h2>
        <p>Lorem Ipsum is simply dummy text of the printing and typesetting industry. Lorem Ipsum has been the industry's standard dummy text ever since the 1500s, when an unknown printer took a galley of type and scrambled it to make a type specimen book. It has survived not only five centuries, but also the leap into electronic typesetting, remaining essentially unchanged. It was popularised in the 1960s with the release of Letraset sheets containing Lorem Ipsum passages.</p>
      </div>
      <div class="block block--spaced">
        <h2 class="section-title">Key Takeaways</h2>
        <p>Lorem Ipsum is simply dummy text of the printing and typesetting industry. Lorem Ipsum has been the industry's standard dummy text ever since the 1500s, when an unknown printer took a galley of type and scrambled it to make a type specimen book.</p>
        <p>It has survived not only five centuries, but also the leap into electronic typesetting, remaining essentially unchanged. It was popularised in the 1960s with the release of Letraset sheets containing Lorem Ipsum passages. Lorem Ipsum is simply dummy text of the printing and typesetting industry.</p>
      </div>
      <div class="topic">
        <h3 class="topic-title">Initial Access</h3>
        <p>Lorem Ipsum is simply dummy text of the printing and typesetting industry. Lorem Ipsum has been the industry's standard dummy text ever since the 1500s, when an unknown printer took a galley of type and scrambled it to make a type specimen book.</p>
      </div>
      <div class="topic">
        <h3 class="topic-title">Execution</h3>
        <p>It has survived not only five centuries, but also the leap into electronic typesetting, remaining essentially unchanged. It was popularised in the 1960s with the release of Letraset sheets containing Lorem Ipsum passages. Lorem Ipsum is simply dummy text of the printing and typesetting industry.</p>
      </div>
      <div class="topic">
        <h3 class="topic-title">Capabilities</h3>
        <p>It has survived not only five centuries, but also the leap into electronic typesetting, remaining essentially unchanged. It was popularised in the 1960s with the release of Letraset sheets containing Lorem Ipsum passages. Lorem Ipsum is simply dummy text of the printing and typesetting industry.</p>
        <p>It has survived not only five centuries, but also the leap into electronic typesetting, remaining essentially unchanged. It was popularised in the 1960s with the release of Letraset sheets containing Lorem Ipsum passages. Lorem Ipsum is simply dummy text of the printing and typesetting industry.</p>
      </div>
    </section>

    <ul class="features">
      <li class="feature"><svg viewBox="0 0 14 14"><path d="M7 1c1 3 4 4 4 8a4 4 0 0 1-8 0c0-2 1-3 2-4 0 2 1 2 1 2 0-3 1-4 1-6z"/></svg><span class="feature__top">Systems</span><span class="feature__bottom">Emergency-Proof</span></li>
      <li class="feature"><svg viewBox="0 0 14 14"><rect x="1" y="3" width="12" height="9" rx="1.5"/></svg><span class="feature__top">24/7 Technical</span><span class="feature__bottom">Support</span></li>
      <li class="feature"><svg viewBox="0 0 14 14"><circle cx="4" cy="5" r="2"/><circle cx="10" cy="5" r="2"/><circle cx="7" cy="4" r="2.3"/><rect x="1" y="8" width="12" height="4" rx="2"/></svg><span class="feature__top">Best Equipment</span><span class="feature__bottom">And Systems</span></li>
      <li class="feature"><svg viewBox="0 0 14 14"><path d="M4 12a3 3 0 0 1 0-6 3.5 3.5 0 0 1 6.5-1A3 3 0 0 1 11 12z"/></svg><span class="feature__top">Best And Easiest To</span><span class="feature__bottom">Use Applications</span></li>
      <li class="feature"><svg viewBox="0 0 14 14"><rect x="6" y="0" width="2" height="14" transform="rotate(45 7 7)"/><rect x="6" y="0" width="2" height="14" transform="rotate(-45 7 7)"/></svg><span class="feature__top">Systems Healthy &amp;</span><span class="feature__bottom">Running Smoothly</span></li>
      <li class="feature"><svg viewBox="0 0 14 14"><path d="M4 11a3 3 0 0 1 0-6 3.5 3.5 0 0 1 6.5-1A3 3 0 0 1 11 11z"/></svg><span class="feature__top">Performance &amp;</span><span class="feature__bottom">Flexibility</span></li>
    </ul>

    <footer class="contact-bar">
      <svg class="contact-bar__shape" width="424" height="29" viewBox="0 0 424 29">
        <polygon points="0,0 86,0 78,29 0,29" fill="var(--brand-red)"/>
        <polygon points="91,0 424,0 424,29 83,29" fill="var(--bar-grey)"/>
      </svg>
      <p class="contact-bar__prompt">Looking for<br>more information</p>
      <div class="contact-list">
        <span class="contact-item"><svg viewBox="0 0 10 10"><circle cx="5" cy="5" r="5"/></svg>555 010 0199-101</span>
        <span class="contact-item"><svg viewBox="0 0 10 10"><circle cx="5" cy="5" r="5"/></svg>hello@brightlinenet.com</span>
        <span class="contact-item"><svg viewBox="0 0 10 10"><circle cx="5" cy="5" r="5"/></svg>www.brightlinenet-example.com</span>
      </div>
    </footer>
  </article>

  <!-- Fact sheet: clean header -->
  <article class="sheet sheet--clean">
    <header class="header">
      <div class="earth-photo" role="img" aria-label="Night view of the Earth from orbit covered by a glowing network of connected points"></div>
      <svg width="424" height="90" viewBox="0 0 424 90">
        <polygon points="0,65 193,65 217,0 224,0 198,69 0,69" fill="var(--bar-grey)"/>
        <rect x="198" y="66" width="226" height="3" fill="var(--bar-grey)"/>
      </svg>
      <div class="brand">
        <span class="brand__mark"></span>
        <span class="brand__name">Brightline Networks</span>
      </div>
      <p class="tagline">We Make Your IT-problems <span class="tagline__accent">Go Away For Good.</span></p>
    </header>

    <section class="content">
      <div class="block">
        <h2 class="section-title">Summary</h2>
        <p>Lorem Ipsum is simply dummy text of the printing and typesetting industry. Lorem Ipsum has been the industry's standard dummy text ever since the 1500s, when an unknown printer took a galley of type and scrambled it to make a type specimen book. It has survived not only five centuries, but also the leap into electronic typesetting, remaining essentially unchanged. It was popularised in the 1960s with the release of Letraset sheets containing Lorem Ipsum passages.</p>
      </div>
      <div class="block block--spaced">
        <h2 class="section-title">Key Takeaways</h2>
        <p>Lorem Ipsum is simply dummy text of the printing and typesetting industry. Lorem Ipsum has been the industry's standard dummy text ever since the 1500s, when an unknown printer took a galley of type and scrambled it to make a type specimen book.</p>
        <p>It has survived not only five centuries, but also the leap into electronic typesetting, remaining essentially unchanged. It was popularised in the 1960s with the release of Letraset sheets containing Lorem Ipsum passages. Lorem Ipsum is simply dummy text of the printing and typesetting industry.</p>
      </div>
      <div class="topic">
        <h3 class="topic-title">Initial Access</h3>
        <p>Lorem Ipsum is simply dummy text of the printing and typesetting industry. Lorem Ipsum has been the industry's standard dummy text ever since the 1500s, when an unknown printer took a galley of type and scrambled it to make a type specimen book.</p>
      </div>
      <div class="topic">
        <h3 class="topic-title">Execution</h3>
        <p>It has survived not only five centuries, but also the leap into electronic typesetting, remaining essentially unchanged. It was popularised in the 1960s with the release of Letraset sheets containing Lorem Ipsum passages. Lorem Ipsum is simply dummy text of the printing and typesetting industry.</p>
      </div>
      <div class="topic">
        <h3 class="topic-title">Capabilities</h3>
        <p>It has survived not only five centuries, but also the leap into electronic typesetting, remaining essentially unchanged. It was popularised in the 1960s with the release of Letraset sheets containing Lorem Ipsum passages. Lorem Ipsum is simply dummy text of the printing and typesetting industry.</p>
        <p>It has survived not only five centuries, but also the leap into electronic typesetting, remaining essentially unchanged. It was popularised in the 1960s with the release of Letraset sheets containing Lorem Ipsum passages. Lorem Ipsum is simply dummy text of the printing and typesetting industry.</p>
      </div>
    </section>

    <ul class="features">
      <li class="feature"><svg viewBox="0 0 14 14"><path d="M7 1c1 3 4 4 4 8a4 4 0 0 1-8 0c0-2 1-3 2-4 0 2 1 2 1 2 0-3 1-4 1-6z"/></svg><span class="feature__top">Systems</span><span class="feature__bottom">Emergency-Proof</span></li>
      <li class="feature"><svg viewBox="0 0 14 14"><rect x="1" y="3" width="12" height="9" rx="1.5"/></svg><span class="feature__top">24/7 Technical</span><span class="feature__bottom">Support</span></li>
      <li class="feature"><svg viewBox="0 0 14 14"><circle cx="4" cy="5" r="2"/><circle cx="10" cy="5" r="2"/><circle cx="7" cy="4" r="2.3"/><rect x="1" y="8" width="12" height="4" rx="2"/></svg><span class="feature__top">Best Equipment</span><span class="feature__bottom">And Systems</span></li>
      <li class="feature"><svg viewBox="0 0 14 14"><path d="M4 12a3 3 0 0 1 0-6 3.5 3.5 0 0 1 6.5-1A3 3 0 0 1 11 12z"/></svg><span class="feature__top">Best And Easiest To</span><span class="feature__bottom">Use Applications</span></li>
      <li class="feature"><svg viewBox="0 0 14 14"><rect x="6" y="0" width="2" height="14" transform="rotate(45 7 7)"/><rect x="6" y="0" width="2" height="14" transform="rotate(-45 7 7)"/></svg><span class="feature__top">Systems Healthy &amp;</span><span class="feature__bottom">Running Smoothly</span></li>
      <li class="feature"><svg viewBox="0 0 14 14"><path d="M4 11a3 3 0 0 1 0-6 3.5 3.5 0 0 1 6.5-1A3 3 0 0 1 11 11z"/></svg><span class="feature__top">Performance &amp;</span><span class="feature__bottom">Flexibility</span></li>
    </ul>

    <footer class="contact-bar">
      <svg class="contact-bar__shape" width="424" height="29" viewBox="0 0 424 29">
        <polygon points="0,0 86,0 78,29 0,29" fill="var(--brand-red)"/>
        <polygon points="91,0 424,0 424,29 83,29" fill="var(--bar-grey)"/>
      </svg>
      <p class="contact-bar__prompt">Looking for<br>more information</p>
      <div class="contact-list">
        <span class="contact-item"><svg viewBox="0 0 10 10"><circle cx="5" cy="5" r="5"/></svg>555 010 0199-101</span>
        <span class="contact-item"><svg viewBox="0 0 10 10"><circle cx="5" cy="5" r="5"/></svg>hello@brightlinenet.com</span>
        <span class="contact-item"><svg viewBox="0 0 10 10"><circle cx="5" cy="5" r="5"/></svg>www.brightlinenet-example.com</span>
      </div>
    </footer>
  </article>

</main>
</body>
</html>
```